Quorvix Letter head

Quorvix is a young and energetic software development consultancy. We spend our time working with clients to turn what ever is in their heads in to software.
We are trying to create an image of a high class software boutique who build class leading bespoke solutions.
We need a sharp letter head that looks great on high quality media.
We like bold colours and distinctive design. So show us what you can do.
Industry/Entity Type
Software
Requirements
Must have
- Our company is based in the UK and are requried to have on the paper somewhere the following information:
* Registered company name: Quorvix Ltd
* Registered company number
* VAT registration number
In addition we also want the following:
* An email address
* Telephone number
* Website address
An example of what some pages have in their footer is something like the following:
Quorvix Ltd is registered in England and Wales. Reg. no: 5316274
Registered office: 48 Cobblewick Road, Harlow Essex, CM93TP. Tel: 07712365081
You do not have to use this sentance but please make sure your design incorporates accommodates the requirements for UK based companies

```html
<!DOCTYPE html>
<html lang="en">
<head>
<meta charset="utf-8">
<title>Quorvix Letterhead</title>
<link rel="stylesheet" href="https://fonts.googleapis.com/css2?family=Exo+2:wght@300;400&display=swap">
<style>
  :root {
    --brand-red: #c01f2f;
    --paper: #ffffff;
    --footer-text: #ffffff;
  }
  html, body {
    margin: 0;
    padding: 0;
    width: 971px;
    height: 1200px;
    overflow: hidden;
    background: var(--paper);
  }
  .letterhead {
    position: relative;
    width: 971px;
    height: 1200px;
    background: var(--paper);
    font-family: "Exo 2", sans-serif;
  }
  .letterhead__brand {
    position: absolute;
    top: 66px;
    left: 0;
    width: 100%;
    text-align: center;
    margin: 0;
    font-size: 84px;
    font-weight: 400;
    line-height: 1;
    letter-spacing: 2px;
    color: var(--brand-red);
    text-transform: uppercase;
  }
  .letterhead__legal {
    position: absolute;
    left: 0;
    top: 1120px;
    width: 100%;
    margin: 0;
    text-align: center;
    font-size: 11px;
    font-weight: 400;
    letter-spacing: 0.3px;
    line-height: 14px;
    color: var(--brand-red);
  }
  .letterhead__footer {
    position: absolute;
    left: 0;
    top: 1144px;
    width: 100%;
    height: 33px;
    background: var(--brand-red);
    color: var(--footer-text);
    display: flex;
    align-items: center;
    justify-content: space-between;
    box-sizing: border-box;
    padding: 0 49px;
    font-size: 13px;
    font-weight: 300;
    letter-spacing: 0.3px;
    text-transform: uppercase;
    white-space: nowrap;
  }
  .letterhead__rule {
    position: absolute;
    left: 0;
    width: 100%;
    height: 2px;
    background: var(--brand-red);
  }
  .letterhead__rule--upper { top: 1184px; }
  .letterhead__rule--lower { top: 1191px; }
</style>
</head>
<body>
  <main class="letterhead">
    <h1 class="letterhead__brand">Quorvix</h1>
    <p class="letterhead__legal">Quorvix Ltd is registered in England and Wales. Reg. no: 5316274. VAT reg. no: GB 284 7719 36</p>
    <footer class="letterhead__footer">
      <span class="footer__address">48 Cobblewick Road, Harlow Essex, CM93TP.</span>
      <span class="footer__phone">Tel: 07712365081</span>
      <span class="footer__email">Email: info@quorvix.com</span>
      <span class="footer__web">www.quorvix.com</span>
    </footer>
    <div class="letterhead__rule letterhead__rule--upper"></div>
    <div class="letterhead__rule letterhead__rule--lower"></div>
  </main>
</body>
</html>
```